Lumo Voyages
business cards & letterhead
Lumo Voyages -
Creative Brief
Bright & Fun-filled
Corinne Maddox
58214 Birchwood Ln Rockville, MD 20817
lumovoyages@quellnet.example

```html
<!DOCTYPE html>
<html lang="en">
<head>
<meta charset="utf-8">
<title>Lumo Voyages – Business Card</title>
<link href="https://fonts.googleapis.com/css2?family=Arimo:wght@400;700&display=swap" rel="stylesheet">
<style>
  :root {
    --backdrop: #e9e6e1;
    --card: #ffffff;
    --brand-blue: #1f6fb8;
    --brand-green: #8cc63f;
    --text-grey: #6b6b6b;
    --divider: #d9d9d9;
  }
  * { margin: 0; padding: 0; box-sizing: border-box; }
  html, body {
    width: 1200px;
    height: 780px;
    overflow: hidden;
    background: var(--backdrop);
    font-family: "Arimo", Arial, sans-serif;
  }
  .business-card {
    position: absolute;
    left: 80px;
    top: 93px;
    width: 1040px;
    height: 594px;
    background: var(--card);
    border-radius: 40px;
    box-shadow: 0 10px 30px rgba(0,0,0,0.18);
  }
  .brand {
    position: absolute;
    left: 70px;
    top: 242px;
    display: flex;
    align-items: center;
    gap: 22px;
  }
  .brand-dot {
    width: 110px;
    height: 110px;
    border-radius: 50%;
    background: var(--brand-green);
  }
  .brand-name {
    font-size: 42px;
    font-weight: 700;
    color: var(--brand-blue);
    white-space: nowrap;
  }
  .divider {
    position: absolute;
    left: 580px;
    top: 40px;
    width: 2px;
    height: 514px;
    background: linear-gradient(to bottom, transparent, var(--divider) 15%, var(--divider) 85%, transparent);
    box-shadow: 3px 0 6px rgba(0,0,0,0.06);
  }
  .contact {
    position: absolute;
    left: 625px;
    top: 118px;
  }
  .contact-name {
    font-size: 34px;
    font-weight: 700;
    color: var(--brand-blue);
    margin-bottom: 44px;
  }
  .contact-address {
    font-size: 24px;
    line-height: 34px;
    color: var(--text-grey);
    margin-bottom: 48px;
  }
  .contact-line {
    display: flex;
    align-items: center;
    gap: 12px;
    font-size: 24px;
    color: var(--text-grey);
    margin-bottom: 22px;
  }
  .contact-icon {
    width: 26px;
    height: 26px;
    flex: none;
  }
</style>
</head>
<body>
  <div class="business-card">
    <div class="brand">
      <div class="brand-dot"></div>
      <div class="brand-name">Lumo Voyages</div>
    </div>

    <div class="divider"></div>

    <div class="contact">
      <div class="contact-name">Corinne Maddox</div>
      <div class="contact-address">58214 Birchwood Ln<br>Rockville, MD 20817</div>
      <div class="contact-line">
        <svg class="contact-icon" viewBox="0 0 24 24" aria-hidden="true">
          <path d="M6.6 10.8a15.1 15.1 0 0 0 6.6 6.6l2.2-2.2a1 1 0 0 1 1-.25 11.4 11.4 0 0 0 3.6.57 1 1 0 0 1 1 1V20a1 1 0 0 1-1 1A17 17 0 0 1 3 4a1 1 0 0 1 1-1h3.5a1 1 0 0 1 1 1c0 1.25.2 2.45.57 3.57a1 1 0 0 1-.25 1z" fill="var(--brand-blue)"/>
        </svg>
        <span>301-555-0192</span>
      </div>
      <div class="contact-line">
        <svg class="contact-icon" viewBox="0 0 24 24" aria-hidden="true">
          <circle cx="12" cy="12" r="4" fill="none" stroke="var(--brand-blue)" stroke-width="2.4"/>
          <path d="M16 8v5.5a2.5 2.5 0 0 0 5 0V12a9 9 0 1 0-3.6 7.2" fill="none" stroke="var(--brand-blue)" stroke-width="2.4" stroke-linecap="round"/>
        </svg>
        <span>lumovoyages@quellnet.example</span>
      </div>
    </div>
  </div>
</body>
</html>
```